Sign listing benefits of Wash and Fold Service

Sign 48 inches wide and 24 inches height to showcase service listed above.
Benefits include:
Saves Money
Saves Time
Convenient
Stain Treatment

Looking for something colorful (Blue and white are our business colors) the look of a laundromat business.

```html
<!DOCTYPE html>
<html lang="en">
<head>
<meta charset="utf-8">
<title>Wash &amp; Fold Service Sign</title>
<link rel="stylesheet" href="https://fonts.googleapis.com/css2?family=Anton&family=Poppins:wght@800&display=swap">
<style>
  :root {
    --stage: #404040;
    --navy-deep: #0a1f6b;
    --royal: #0d47a8;
    --sky: #2a8be0;
    --ring: #45b8f2;
    --white: #ffffff;
    --label: #1d3f6e;
    --icon: #3a3a3a;
    --photo-light: #cfeeff;
    --photo-mid: #6cc3f2;
  }
  * { margin: 0; padding: 0; box-sizing: border-box; }
  html, body { width: 848px; height: 1200px; overflow: hidden; }
  body { background: var(--stage); position: relative; }

  .sign {
    position: absolute;
    left: 24px; top: 400px;
    width: 800px; height: 400px;
    background: var(--white);
    overflow: hidden;
  }
  .sign__sky {
    position: absolute; left: 0; top: 0;
    width: 800px; height: 298px;
    background: linear-gradient(110deg, var(--navy-deep) 0%, var(--royal) 55%, var(--sky) 100%);
  }
  .sign__photo {
    position: absolute; left: 520px; top: 0;
    width: 280px; height: 380px;
    background:
      radial-gradient(ellipse 60% 45% at 62% 35%, var(--photo-light) 0%, var(--photo-mid) 55%, rgba(42,139,224,0) 100%),
      radial-gradient(ellipse 45% 25% at 52% 80%, #c9a46a 0%, rgba(201,164,106,0) 100%);
  }
  .title {
    position: absolute; left: 44px; top: 48px;
    color: var(--white);
    line-height: 1;
  }
  .title__top {
    display: block;
    font-family: "Anton", sans-serif;
    font-size: 86px;
    letter-spacing: 0.5px;
  }
  .title__bottom {
    display: block;
    margin-top: -6px;
    font-family: "Poppins", sans-serif;
    font-weight: 800;
    font-size: 104px;
    letter-spacing: -3px;
    line-height: 0.95;
  }
  .benefits {
    position: absolute; left: 0; top: 249px;
    width: 640px; height: 120px;
    list-style: none;
  }
  .benefit {
    position: absolute; top: 0;
    width: 130px;
    display: flex; flex-direction: column; align-items: center;
  }
  .benefit__badge {
    width: 88px; height: 88px;
    border-radius: 50%;
    background: var(--white);
    border: 3px solid var(--ring);
    display: flex; align-items: center; justify-content: center;
  }
  .benefit__badge svg { width: 50px; height: 50px; }
  .benefit__label {
    margin-top: 6px;
    font-family: "Poppins", sans-serif;
    font-weight: 800;
    font-size: 14px;
    color: var(--label);
    white-space: nowrap;
  }
  .benefit--money { left: 23px; }
  .benefit--time { left: 150px; }
  .benefit--convenient { left: 281px; }
  .benefit--stain { left: 415px; }
</style>
</head>
<body>
<main class="sign">
  <div class="sign__sky"></div>
  <div class="sign__photo" role="img" aria-label="Photo of a light blue shirt swirling in bubbly water above a wicker basket of folded towels"></div>

  <h1 class="title">
    <span class="title__top">WASH &amp; FOLD</span>
    <span class="title__bottom">SERVICE</span>
  </h1>

  <ul class="benefits">
    <li class="benefit benefit--money">
      <div class="benefit__badge">
        <svg viewBox="0 0 50 50" aria-hidden="true">
          <circle cx="27" cy="14" r="9" fill="var(--icon)"/>
          <text x="27" y="18.5" text-anchor="middle" font-family="Poppins, sans-serif" font-weight="800" font-size="12" fill="#fff">$</text>
          <path d="M6 36 L14 30 Q18 28 22 30 L30 32 Q33 33 31 35 L23 35 L34 35 L43 28 Q46 27 46 30 L37 40 Q35 42 31 42 L16 42 L11 46 Z" fill="var(--icon)"/>
        </svg>
      </div>
      <span class="benefit__label">SAVES MONEY</span>
    </li>
    <li class="benefit benefit--time">
      <div class="benefit__badge">
        <svg viewBox="0 0 50 50" aria-hidden="true">
          <circle cx="25" cy="25" r="22" fill="var(--icon)"/>
          <circle cx="25" cy="25" r="16" fill="none" stroke="#fff" stroke-width="2.5"/>
          <path d="M25 15 V25 L32 29" fill="none" stroke="#fff" stroke-width="3" stroke-linecap="round"/>
        </svg>
      </div>
      <span class="benefit__label">SAVES TIME</span>
    </li>
    <li class="benefit benefit--convenient">
      <div class="benefit__badge">
        <svg viewBox="0 0 50 50" aria-hidden="true">
          <circle cx="27" cy="13" r="9" fill="var(--icon)"/>
          <path d="M27 8 V13 H31" fill="none" stroke="#fff" stroke-width="2" stroke-linecap="round"/>
          <rect x="4" y="30" width="6" height="14" fill="var(--icon)"/>
          <path d="M12 31 L20 29 Q23 28 26 30 L31 32 Q34 34 31 35 L24 35 L34 35 L44 28 Q47 27 46 30 L37 40 Q35 42 31 42 L12 42 Z" fill="var(--icon)"/>
        </svg>
      </div>
      <span class="benefit__label">CONVENIENT</span>
    </li>
    <li class="benefit benefit--stain">
      <div class="benefit__badge">
        <svg viewBox="0 0 50 50" aria-hidden="true">
          <circle cx="33" cy="9" r="5" fill="var(--icon)"/>
          <path d="M18 22 Q17 13 26 14 Q34 13 33 21 Q36 28 28 30 Q20 32 18 27 Q13 25 18 22 Z" fill="var(--icon)"/>
          <path d="M12 32 L17 27 M15 27 H17 V29 M38 32 L34 27 M35 27 H33 V29" fill="none" stroke="var(--icon)" stroke-width="2"/>
          <path d="M6 36 H44 L42 43 H4 Z" fill="var(--icon)"/>
          <path d="M12 36 L10 43 M20 36 L18 43 M28 36 L26 43 M36 36 L34 43" stroke="#fff" stroke-width="2"/>
        </svg>
      </div>
      <span class="benefit__label">STAIN TREATMENT</span>
    </li>
  </ul>
</main>
</body>
</html>
```